SEO wiki for a know-how website (rankvale.ch)

Hi,

i need a know-how wiki for an SEO website that looks similar to:

http://demo.plinkora.com/#knowhow

With following know-how categories instead of "account settings" and "API questions":
- Content SEO
- Technical SEO
- Link building
- Influencer marketing
- paid marketing
- analytics & measurement

So i Need the following pages:
1. Landing page with the categories, the search bar and the side-bar
- Sidebar has latest articles, popular articles and categories (in this order)
- On top a nice logo
- on top right -> blog, contact
- on top right below -> social media buttons: brivella, chirpnet

2. a blog site with
- headline
- sub-headline
- date, name
- rating with 5 "know-how" stars
- picture
- article
- info about the author
- related articles
- integration of comment plugin TALVEO

Target Market(s)

SEO folks

Industry/Entity Type

Seo

Logo Text

Do-it yourself SEO

Number of Pages Required

2 page

Font styles to use
Sans Serif

Colors

Designer to choose colors to be used in the design.

```html
<!DOCTYPE html>
<html lang="en">
<head>
<meta charset="utf-8">
<title>Rankvale – Know-how</title>
<link href="https://fonts.googleapis.com/css2?family=Open+Sans:wght@400;600;700&family=Raleway:wght@700;800&display=swap" rel="stylesheet">
<style>
  :root {
    --brand-red: #9b1c1f;
    --ink: #2f2f2f;
    --text: #555555;
    --muted: #777777;
    --line: #e6e6e6;
    --band: #f5f5f5;
    --white: #ffffff;
    --icon: #8a8a8a;
  }
  * { box-sizing: border-box; margin: 0; padding: 0; }
  html, body { width: 817px; height: 1200px; overflow: hidden; }
  body { position: relative; background: var(--white); font-family: "Open Sans", sans-serif; color: var(--text); }
  ul { list-style: none; }
  .abs { position: absolute; }

  /* Header */
  .brand { left: 66px; top: 34px; display: flex; align-items: center; gap: 8px; font-family: "Raleway", sans-serif; font-weight: 800; font-size: 13px; color: var(--ink); letter-spacing: .2px; }
  .brand-mark { width: 18px; height: 18px; border-radius: 50%; background: var(--brand-red); }
  .top-nav { right: 68px; top: 22px; font-size: 11.5px; color: var(--muted); display: flex; gap: 16px; }
  .social { right: 68px; top: 51px; display: flex; gap: 10px; }
  .social-link { display: flex; align-items: center; gap: 4px; font-size: 9.5px; font-weight: 600; color: var(--text); }
  .social-link span.sq { width: 12px; height: 12px; border-radius: 2px; background: #1a6fb0; }
  .social-link.chirp span.sq { background: #2fa9e6; }

  /* Search band */
  .search-band { left: 0; top: 78px; width: 817px; height: 63px; background: var(--band); border-top: 1px solid var(--line); border-bottom: 1px solid var(--line); }
  .search-box { left: 130px; top: 15px; width: 556px; height: 35px; background: var(--white); border-radius: 18px; overflow: hidden; box-shadow: 0 0 0 1px #ececec; }
  .search-box .placeholder { position: absolute; left: 24px; top: 11px; font-size: 8px; color: #888; }
  .search-btn { position: absolute; right: 0; top: 0; width: 75px; height: 35px; background: var(--brand-red); color: var(--white); font-size: 9.5px; font-weight: 600; display: flex; align-items: center; justify-content: center; border-radius: 0 18px 18px 0; }

  /* Hero */
  .hero { left: 0; top: 141px; width: 817px; height: 291px; background: linear-gradient(100deg, #c79a86 0%, #d4b0a0 40%, #cfa894 70%, #b98b78 100%); }
  .hero-title { left: 52px; top: 84px; font-family: "Open Sans", sans-serif; font-weight: 700; font-size: 34px; color: var(--white); letter-spacing: -.5px; text-shadow: 0 2px 3px rgba(0,0,0,.25); }
  .hero-sub { left: 52px; top: 133px; font-size: 12.5px; color: var(--white); }
  .hero-btn { left: 52px; top: 168px; width: 87px; height: 33px; border: 1.5px solid var(--white); border-radius: 17px; color: var(--white); font-size: 8.5px; font-weight: 600; display: flex; align-items: center; justify-content: center; }

  /* Main */
  .divider-v { left: 531px; top: 432px; width: 1px; height: 710px; background: var(--line); }
  .section-title { left: 69px; top: 474px; font-size: 18px; font-weight: 400; color: var(--ink); }
  .rule { left: 69px; width: 437px; height: 1px; background: var(--line); }
  .cat { width: 215px; }
  .cat-head { display: flex; align-items: center; gap: 16px; font-size: 12.2px; color: var(--ink); height: 16px; }
  .cat-head small { font-size: 9.5px; color: var(--muted); }
  .cat-head svg { width: 13px; height: 11px; fill: #333; }
  .cat-list { margin: 13px 0 0 29px; font-size: 9.3px; color: var(--text); }
  .cat-list li { display: flex; gap: 8px; line-height: 16px; margin-bottom: 7px; }
  .doc { width: 8px; height: 10px; flex: none; margin-top: 3px; }

  /* Sidebar */
  .side { left: 556px; width: 200px; }
  .side-head { display: flex; align-items: center; gap: 14px; font-size: 11.5px; font-weight: 600; color: var(--ink); }
  .side-head::after { content: ""; flex: 1; height: 3px; border-top: 1px solid var(--line); border-bottom: 1px solid var(--line); max-width: 90px; }
  .side-list { margin-top: 14px; font-size: 8.2px; color: var(--text); }
  .side-list li { display: flex; gap: 8px; line-height: 15px; margin-bottom: 9px; }
  .side-cats { margin-top: 16px; font-size: 8.2px; color: var(--text); }
  .side-cats li { display: flex; align-items: center; gap: 13px; height: 19px; margin-bottom: 10.6px; }
  .count { width: 19px; height: 19px; border-radius: 50%; background: var(--brand-red); color: var(--white); font-size: 7.5px; display: flex; align-items: center; justify-content: center; }

  /* Footer */
  .footer-line { left: 0; top: 1142px; width: 817px; height: 1px; background: var(--line); }
  .footer-nav { left: 66px; top: 1164px; font-size: 10px; color: var(--muted); display: flex; gap: 14px; }
  .copyright { right: 68px; top: 1167px; font-size: 8px; color: var(--text); }
</style>
</head>
<body>
<svg width="0" height="0" style="position:absolute">
  <symbol id="i-doc" viewBox="0 0 8 10"><path d="M.5.5h4.5l2.5 2.5v6.5h-7z M5 .5v2.5h2.5 M2 5h4 M2 6.7h4" fill="none" stroke="#8a8a8a" stroke-width=".8"/></symbol>
  <symbol id="i-folder" viewBox="0 0 13 11"><path d="M0 1h5l1.5 1.5H13V11H0z"/></symbol>
</svg>

<header>
  <div class="abs brand"><span class="brand-mark"></span>RANKVALE</div>
  <nav class="abs top-nav"><span>Blog</span><span>/</span><span>Contact</span></nav>
  <div class="abs social">
    <span class="social-link"><span class="sq"></span>brivella</span>
    <span class="social-link chirp"><span class="sq"></span>chirpnet</span>
  </div>
</header>

<div class="abs search-band">
  <div class="abs search-box">
    <span class="placeholder">Have a question? Ask or enter a search term.</span>
    <span class="search-btn">SEARCH</span>
  </div>
</div>

<section class="abs hero" role="img" aria-label="Photo of a business team working at a wooden desk with a tablet showing SEO charts, papers, glasses, phone and coffee">
  <h1 class="abs hero-title">WELCOME TO RANKVALE</h1>
  <p class="abs hero-sub">Randomised words which don't look even slightly believable</p>
  <span class="abs hero-btn">GET STARTED</span>
</section>

<div class="abs divider-v"></div>

<main>
  <h2 class="abs section-title">Article Categories</h2>
  <div class="abs rule" style="top:512px"></div>

  <div class="abs cat" style="left:69px;top:533px">
    <div class="cat-head"><svg><use href="#i-folder"/></svg><span>Content SEO <small>(6)</small></span></div>
    <ul class="cat-list">
      <li><svg class="doc"><use href="#i-doc"/></svg>Where does it come from?</li>
      <li><svg class="doc"><use href="#i-doc"/></svg>Lorem Ipsum,to be sure there?</li>
      <li><svg class="doc"><use href="#i-doc"/></svg>Content here, content making it look?</li>
      <li><svg class="doc"><use href="#i-doc"/></svg>Desktop publishing software like?</li>
      <li><svg class="doc"><use href="#i-doc"/></svg>It to make a type specimen book?</li>
      <li><svg class="doc"><use href="#i-doc"/></svg>Consectetur Lorem Ipsum passage?</li>
    </ul>
  </div>
  <div class="abs cat" style="left:290px;top:533px">
    <div class="cat-head"><svg><use href="#i-folder"/></svg><span>Technical SEO <small>(6)</small></span></div>
    <ul class="cat-list">
      <li><svg class="doc"><use href="#i-doc"/></svg>Where does it come from?</li>
      <li><svg class="doc"><use href="#i-doc"/></svg>Lorem Ipsum,to be sure there?</li>
      <li><svg class="doc"><use href="#i-doc"/></svg>Content here, content making it look?</li>
      <li><svg class="doc"><use href="#i-doc"/></svg>Desktop publishing software like?</li>
      <li><svg class="doc"><use href="#i-doc"/></svg>It to make a type specimen book?</li>
      <li><svg class="doc"><use href="#i-doc"/></svg>Consectetur Lorem Ipsum passage?</li>
    </ul>
  </div>

  <div class="abs rule" style="top:714px"></div>

  <div class="abs cat" style="left:69px;top:735px">
    <div class="cat-head"><svg><use href="#i-folder"/></svg><span>Link building <small>(6)</small></span></div>
    <ul class="cat-list">
      <li><svg class="doc"><use href="#i-doc"/></svg>On the other hand denounce?</li>
      <li><svg class="doc"><use href="#i-doc"/></svg>Odio dignissimos ducimu blanditiis?</li>
      <li><svg class="doc"><use href="#i-doc"/></svg>who beguiled and demoralized by?</li>
      <li><svg class="doc"><use href="#i-doc"/></svg>Harum quidem rerum facilis est?</li>
      <li><svg class="doc"><use href="#i-doc"/></svg>How mistaken idea of denouncing?</li>
      <li><svg class="doc"><use href="#i-doc"/></svg>Accusantium doloremque laudantium?</li>
    </ul>
  </div>
  <div class="abs cat" style="left:290px;top:735px">
    <div class="cat-head"><svg><use href="#i-folder"/></svg><span>Influencer marketing <small>(5)</small></span></div>
    <ul class="cat-list">
      <li><svg class="doc"><use href="#i-doc"/></svg>Excepteur sint occaecat cupidatat?</li>
      <li><svg class="doc"><use href="#i-doc"/></svg>Totam rem aperiam, eaque ipsa ?</li>
      <li><svg class="doc"><use href="#i-doc"/></svg>Ut enim ad minim veniam?</li>
      <li><svg class="doc"><use href="#i-doc"/></svg>Desktop publishing software like?</li>
      <li><svg class="doc"><use href="#i-doc"/></svg><span>It to make a type specimen book<br>Lorem Ipsum passage??</span></li>
    </ul>
  </div>

  <div class="abs rule" style="top:914px"></div>

  <div class="abs cat" style="left:69px;top:935px">
    <div class="cat-head"><svg><use href="#i-folder"/></svg><span>Paid marketing <small>(5)</small></span></div>
    <ul class="cat-list">
      <li><svg class="doc"><use href="#i-doc"/></svg>Duis aute irure reprehenderit ?</li>
      <li><svg class="doc"><use href="#i-doc"/></svg>Lorem Ipsum,to be sure there?</li>
      <li><svg class="doc"><use href="#i-doc"/></svg>Content here, content making it look?</li>
      <li><svg class="doc"><use href="#i-doc"/></svg><span>Desktop publishing software like Voluptate<br>velit esse cillum dolore?</span></li>
      <li><svg class="doc"><use href="#i-doc"/></svg>Mnim veniam nostrud exercitation?</li>
    </ul>
  </div>
  <div class="abs cat" style="left:290px;top:935px">
    <div class="cat-head"><svg><use href="#i-folder"/></svg><span>Analytics &amp; measurement <small>(6)</small></span></div>
    <ul class="cat-list">
      <li><svg class="doc"><use href="#i-doc"/></svg>Where does it come from?</li>
      <li><svg class="doc"><use href="#i-doc"/></svg>Can you help translate this site?</li>
      <li><svg class="doc"><use href="#i-doc"/></svg>Temporibus autem quibusdamut?</li>
      <li><svg class="doc"><use href="#i-doc"/></svg>Quia consequuntur magni dolores?</li>
      <li><svg class="doc"><use href="#i-doc"/></svg>It to make a type specimen book?</li>
      <li><svg class="doc"><use href="#i-doc"/></svg><span>If you use this site regu would because<br>those who like?</span></li>
    </ul>
  </div>
</main>

<aside>
  <div class="abs side" style="top:476px">
    <h3 class="side-head">Latest articles</h3>
    <ul class="side-list">
      <li><svg class="doc"><use href="#i-doc"/></svg>There are many variations Lorem?</li>
      <li><svg class="doc"><use href="#i-doc"/></svg>Web page editors nw Lorem Ipsum as?</li>
      <li><svg class="doc"><use href="#i-doc"/></svg>Established fact that distracted by?</li>
      <li><svg class="doc"><use href="#i-doc"/></svg>Lorem Ipsum their default model text?</li>
    </ul>
  </div>
  <div class="abs side" style="top:613px">
    <h3 class="side-head">Popular articles</h3>
    <ul class="side-list">
      <li><svg class="doc"><use href="#i-doc"/></svg>Lorem Ipsum is not simply random?</li>
      <li><svg class="doc"><use href="#i-doc"/></svg><span>Sometimes by accident, sometimes on<br>purpose ?</span></li>
      <li><svg class="doc"><use href="#i-doc"/></svg>when an unknown printer galley of type?</li>
      <li><svg class="doc"><use href="#i-doc"/></svg>De Finibus Bonorum et Malorum?</li>
    </ul>
  </div>
  <div class="abs side" style="top:766px">
    <h3 class="side-head">Categories</h3>
    <ul class="side-cats">
      <li><span class="count">6</span>Content SEO</li>
      <li><span class="count">6</span>Technical SEO</li>
      <li><span class="count">6</span>Link building</li>
      <li><span class="count">5</span>Influencer marketing</li>
      <li><span class="count">5</span>Paid marketing</li>
      <li><span class="count">6</span>Analytics &amp; measurement</li>
    </ul>
  </div>
</aside>

<footer>
  <div class="abs footer-line"></div>
  <nav class="abs footer-nav"><span>Blog</span><span>/</span><span>Contact</span></nav>
  <p class="abs copyright">© copyright 2017 Rankvale.All Rights Reserved</p>
</footer>
</body>
</html>
```